Quorvix Letter head

Quorvix is a young and energetic software development consultancy. We spend our time working with clients to turn what ever is in their heads in to software.
We are trying to create an image of a high class software boutique who build class leading bespoke solutions.
We need a sharp letter head that looks great on high quality media.
We like bold colours and distinctive design. So show us what you can do.
Industry/Entity Type
Software
Requirements
Must have
- Our company is based in the UK and are requried to have on the paper somewhere the following information:
* Registered company name: Quorvix Ltd
* Registered company number
* VAT registration number
In addition we also want the following:
* An email address
* Telephone number
* Website address
An example of what some pages have in their footer is something like the following:
Quorvix Ltd is registered in England and Wales. Reg. no: 5316274
Registered office: 48 Cobblewick Road, Harlow Essex, CM93TP. Tel: 07712365081
You do not have to use this sentance but please make sure your design incorporates accommodates the requirements for UK based companies

```html
<!DOCTYPE html>
<html lang="en">
<head>
<meta charset="utf-8">
<title>Quorvix Letterhead</title>
<link rel="stylesheet" href="https://fonts.googleapis.com/css2?family=Source+Sans+3:wght@300;400;600&display=swap">
<style>
  :root {
    --backdrop: #858483;
    --paper: #ffffff;
    --brand-red: #a8232e;
    --stripe-grey: #c4c4c4;
    --body-text: #4a4a4a;
    --footer-text: #bdbdbd;
  }
  * { margin: 0; padding: 0; box-sizing: border-box; }
  html, body {
    width: 849px;
    height: 1200px;
    overflow: hidden;
    background: var(--backdrop);
    font-family: "Source Sans 3", sans-serif;
  }
  .letterhead {
    position: absolute;
    left: 125px;
    top: 175px;
    width: 600px;
    height: 850px;
    background: var(--paper);
  }
  .edge-stripes {
    position: absolute;
    right: 0;
    top: 0;
    width: 26px;
    height: 850px;
  }
  .brand-name {
    position: absolute;
    left: 33px;
    top: 36px;
    font-size: 34px;
    font-weight: 400;
    letter-spacing: 0.5px;
    color: var(--brand-red);
    line-height: 1;
  }
  .letter-body {
    position: absolute;
    left: 46px;
    top: 205px;
    width: 460px;
    font-size: 11px;
    font-weight: 300;
    line-height: 14.3px;
    color: var(--body-text);
    text-align: justify;
  }
  .letter-body p { margin-bottom: 14.3px; }
  .letter-body .salutation { font-weight: 600; margin-bottom: 0; color: #333; }
  .letter-body .product-list { list-style: none; margin-bottom: 14.3px; text-align: left; }
  .company-footer {
    position: absolute;
    left: 33px;
    top: 824px;
    font-size: 8px;
    font-weight: 300;
    line-height: 11px;
    color: var(--footer-text);
  }
</style>
</head>
<body>
  <main class="letterhead">
    <svg class="edge-stripes" viewBox="0 0 26 850" aria-hidden="true">
      <polygon points="0,0 12,0 12,180 0,168" fill="var(--stripe-grey)"/>
      <polygon points="0,172 12,185 12,850 0,850" fill="var(--brand-red)"/>
      <polygon points="15,0 26,0 26,196 15,185" fill="var(--stripe-grey)"/>
      <polygon points="15,190 26,201 26,850 15,850" fill="var(--brand-red)"/>
    </svg>

    <div class="brand-name">Quorvix</div>

    <section class="letter-body">
      <p class="salutation">Dear Sirs,</p>
      <p>We are from PT. SENTOSA RIMBA MAKMUR, Tbk. in this case intends to offering as cooperation with CV. TELUK HARAPAN to become a distributor of our products include:</p>
      <ul class="product-list">
        <li>electronic products</li>
        <li>Household furniture fixtures</li>
        <li>Furniture, etc..</li>
      </ul>
      <p>We will provide compensation comparable to the CV. Teluk HARAPAN if willing to become an official distributor of the products of our company.</p>
      <p>Mechanisms of cooperation we can explain further if CV. Teluk HARAPAN interested in the offer of cooperation that we submit.</p>
      <p>Thus this research agreement offer letter we make, for your attention and cooperation we say thank you.</p>
      <p>Nb: We will wait for a copy of Mr.. Bayu Hartono CV as leader. Teluk HARAPAN later than 14 days after this letter Mr.. receive.</p>
    </section>

    <footer class="company-footer">
      <div>Quorvix Ltd is registered in England and Wales. Reg. no: 5316274</div>
      <div>Office: 48 Cobblewick Road, Harlow Essex, CM93TP. Tel: 07712365081</div>
    </footer>
  </main>
</body>
</html>
```